Pitch book for Birchvale Real Estate Investors.

Birchvale Investors is a new real estate investment company focused on multifamily (apartment) investments along the San Francisco Peninsula (in other parts of the world it is also referred to as flats). We need a professional Pitch Book i.e. brochure (digital and print) to raise equity from private investors. Read about “pitch book” on Wikipedia. The profile of the investor is conservative and must qualify as an accredited investor. Think high net worth individuals, CEOs and wealthy retiring couples. The investor that is attracted to real estate invest because it is low risk, produce cash flow and provide solid returns over the long term.

The brochure should convey trust, be highly professional and be clean and crisp. I attach a PowerPoint doc to be used as a copy for the brochure. I also attach a brochure of Harlow Pike – I like the look and feel, think it was designed with InDesign.

We will use the brochure at one-on-one meetings with investors where we will present on a laptop; we also need it in a format so that we can email it, print it and use it to be uploaded as a website.

I prefer the up and down scroll format (like you would do on a Mac) compared to PowerPoint but I am open to suggestions.

The photos I used in the PowerPoint presentation was found on the web, please use your own stock images.

Target Market(s)

High net worth individuals

Industry/Entity Type

Real Estate

Font styles to use
Serif

Requirements
Must have
• See attached Power Point
Nice to have
• See attached HPK brochure, I like the look and feel.
Should not have
• I am open to your ideas.

```html
<!DOCTYPE html>
<html lang="en">
<head>
<meta charset="utf-8">
<title>Birchvale Investors – Pitch Book Spread</title>
<link rel="stylesheet" href="https://fonts.googleapis.com/css2?family=Marcellus+SC&family=Ubuntu:wght@300;400&display=swap">
<style>
  :root {
    --backdrop: #a9a9a9;
    --teal: #5ec1c4;
    --teal-deep: #4fb2b5;
    --panel: rgba(160, 222, 224, 0.55);
    --ink-dark: #1f3a3c;
    --ink-light: #ffffff;
    --photo-sky: #c9ccd0;
    --photo-mid: #8fa9a6;
    --photo-warm: #a2624f;
    --photo-dark: #2d2a2c;
  }
  * { box-sizing: border-box; margin: 0; padding: 0; }
  html, body {
    width: 1200px; height: 805px; overflow: hidden;
    background: var(--backdrop);
    font-family: "Ubuntu", sans-serif;
  }
  .spread {
    position: absolute; left: 90px; top: 60px;
    width: 1020px; height: 685px;
    display: flex;
    box-shadow: 0 10px 30px rgba(0,0,0,0.25);
  }
  .page { position: relative; width: 510px; height: 100%; overflow: hidden; }

  /* Left page */
  .page--opportunity .photo {
    position: absolute; inset: 0;
    background:
      linear-gradient(180deg, rgba(0,0,0,0) 70%, var(--photo-dark) 100%),
      linear-gradient(90deg, var(--photo-sky) 0%, #b9a9a4 25%, var(--photo-mid) 45%, #b5c3be 70%, #96aaa6 100%);
  }
  .page--opportunity .photo::after {
    content: ""; position: absolute; left: 0; right: 0; bottom: 0; height: 140px;
    background: linear-gradient(180deg, var(--photo-warm) 0%, #5a3a36 35%, var(--photo-dark) 100%);
    opacity: 0.85;
  }
  .opportunity-panel {
    position: absolute; left: 80px; top: 175px; width: 430px; height: 300px;
    background: var(--panel);
    clip-path: polygon(0 0, 100% 0, 100% 82%, 92% 100%, 8% 100%, 0 88%);
    padding: 20px 40px 0 38px;
    color: var(--ink-light);
  }
  .opportunity-panel .title {
    font-family: "Marcellus SC", serif; font-weight: 400;
    font-size: 24px; letter-spacing: 2px; color: var(--ink-dark);
    text-align: right;
  }
  .tagline {
    font-size: 12.5px; color: var(--ink-dark); text-align: right; margin-top: -2px;
  }
  .opportunity-panel p, .opportunity-panel li { font-size: 13px; line-height: 1.35; font-weight: 300; }
  .opportunity-panel .lead { margin-top: 28px; }
  .opportunity-panel .question { margin-top: 10px; }
  .opportunity-panel ul { margin: 8px 0 0 18px; }

  /* Right page */
  .page--mission { background: var(--teal); padding: 38px 46px 0 48px; color: var(--ink-light); }
  .page--mission::before {
    content: ""; position: absolute; left: 0; top: 0; bottom: 0; width: 24px;
    background: linear-gradient(90deg, rgba(0,0,0,0.12), rgba(0,0,0,0));
  }
  .mission-title {
    font-family: "Marcellus SC", serif; font-weight: 400;
    font-size: 20px; letter-spacing: 1.5px; color: var(--ink-dark); line-height: 1.3;
  }
  .mission-title .aside { font-family: "Ubuntu", sans-serif; font-size: 12px; letter-spacing: 0; }
  .mission-body { padding: 0 14px 0 40px; }
  .mission-body p, .mission-body li { font-size: 13px; line-height: 1.35; font-weight: 300; }
  .mission-body .intro { margin-top: 30px; }
  .mission-body h3 { font-weight: 300; font-size: 18px; line-height: 1.2; margin: 20px 0 14px -8px; }
  .mission-body .only { margin-top: 22px; }
  .mission-body ul { margin: 2px 0 0 18px; }
</style>
</head>
<body>
  <main class="spread">
    <section class="page page--opportunity">
      <div class="photo" role="img" aria-label="Photograph of a green-domed Victorian corner building on a San Francisco street at dusk"></div>
      <div class="opportunity-panel">
        <h2 class="title">Your Opportunity</h2>
        <p class="tagline">...safety, cash flow and appreciation</p>
        <p class="lead">Birchvale Investors is pleased to offer you the opportunity to invest in the San Francisco Peninsula multifamily real estate market.</p>
        <p class="question">Why invest and why here?</p>
        <ul>
          <li>Investing in real estate is recognized as a significant wealth-creation strategy.</li>
          <li>The San Francisco Peninsula is one of the top real estate markets in the world.</li>
          <li>The multifamily asset class is considered a low risk investment.</li>
        </ul>
      </div>
    </section>

    <section class="page page--mission">
      <h2 class="mission-title">Our Mission<span class="aside">... to protect and grow your investment</span><br>Find, Buy, Hold for the Long-Term</h2>
      <div class="mission-body">
        <p class="intro">Birchvale Investors’ core goal is to identify investments that produce consistent cash flow, have long-term value prospects not currently recognized by the market, and once acquired, increase their operational and managerial efficiencies to maximize cash flow and capital appreciation.</p>
        <h3>Why focus on a specific asset class and geography?</h3>
        <p>A focused approach is one of our competitive advantages. With 20 years real estate investment and development experience, Birchvale Investors is a Silicon Valley-based multifamily investment and advisory firm, laser-focused on growing cash flow and lasting value for our clients.</p>
        <p class="only">We invest only:</p>
        <ul>
          <li>In existing properties - we can evaluate existing expenses and rent rolls with more certainty;</li>
          <li>In select San Francisco and Silicon Valley locations - we know the streets and neighborhoods;</li>
          <li>Using low risk core and core plus investment strategies - to reasonably predict cash flow; and</li>
          <li>For the long-term - your investment is a safe-haven that endures market fluctuations.</li>
        </ul>
      </div>
    </section>
  </main>
</body>
</html>
```